Modern two-sided business card for a general enterprise that improves the digital user experience.

Our company based in Switzerland covers all services of the digital customer relationship. We automate online ads to acquire new customers and program mobile apps for more efficient customer care in customer service. We employ specialists in marketing, business management, data science, graphic designers, copywriters, UI and programmers. The new business card is intended to show our comprehensive role and various offering of the entire customer journey.

Company Font: Futura
Main Color: # 283583
Secondary: #fcfaee (and gray variations)
Website: https://vup.ch

As little address information as possible: company name, employee, mobile, email, company web & company phone.

Target Market(s)

C-Level (CEO, CIO, CTO), Head Sales, Head Marketing & Head Customer Service

Industry/Entity Type

Digital Marketing, Online-Marketing, Analytics

Contact Information for Business Card

Requirements
Must have
• Company logo type ": vup" only on one side

```html
<!DOCTYPE html>
<html lang="en">
<head>
<meta charset="utf-8">
<title>VUP business card</title>
<link rel="stylesheet" href="https://fonts.googleapis.com/css2?family=Jost:wght@400;500;700&display=swap">
<style>
  :root {
    --brand-blue: #283583;
    --brand-blue-light: #2f48a8;
    --brand-blue-deep: #1f2d73;
    --back-name: #3a55b8;
    --card-white: #fdfdfd;
    --card-grey: #e4e4e4;
    --ink: #1b1b1b;
    --text-grey: #4a4a4a;
    --stage: #2b2b2d;
  }
  * { box-sizing: border-box; margin: 0; padding: 0; }
  html, body {
    width: 1200px;
    height: 874px;
    overflow: hidden;
  }
  body {
    background: var(--stage);
    font-family: "Jost", "Futura", sans-serif;
    display: flex;
    flex-direction: column;
    align-items: center;
    justify-content: center;
    gap: 40px;
  }
  .card {
    width: 560px;
    height: 350px;
    border-radius: 3px;
    position: relative;
    overflow: hidden;
    box-shadow: 0 12px 30px rgba(0,0,0,.45);
  }

  /* Back side */
  .card-back {
    background: linear-gradient(135deg, var(--brand-blue-light) 0%, var(--brand-blue) 55%, var(--brand-blue-deep) 100%);
    display: flex;
    align-items: center;
    justify-content: center;
  }
  .company-name-large {
    font-size: 110px;
    font-weight: 500;
    line-height: 1;
    letter-spacing: 14px;
    color: var(--back-name);
  }

  /* Front side */
  .card-front {
    background: linear-gradient(120deg, var(--card-white) 0%, #f4f4f4 55%, var(--card-grey) 100%);
    text-align: center;
  }
  .rule {
    position: absolute;
    left: 0;
    right: 0;
    top: 164px;
    height: 1px;
    background: var(--brand-blue);
  }
  .company-name {
    position: absolute;
    top: 46px;
    left: 0;
    right: 0;
    font-size: 50px;
    font-weight: 500;
    line-height: 1;
    letter-spacing: 6px;
    color: var(--ink);
  }
  .person {
    position: absolute;
    top: 116px;
    left: 0;
    right: 0;
    font-size: 24px;
    font-weight: 700;
    letter-spacing: 1px;
    text-transform: uppercase;
    color: var(--brand-blue);
  }
  .icons {
    position: absolute;
    top: 152px;
    left: 0;
    right: 0;
    display: flex;
    justify-content: center;
    gap: 4px;
  }
  .icons svg { width: 24px; height: 24px; display: block; }
  .details {
    position: absolute;
    top: 192px;
    left: 0;
    right: 0;
    font-size: 16px;
    line-height: 23px;
    color: var(--text-grey);
  }
  .details .sep { color: var(--ink); font-weight: 700; margin: 0 5px; }
  .website {
    position: absolute;
    top: 284px;
    left: 0;
    right: 0;
    font-size: 19px;
    font-weight: 700;
    letter-spacing: .5px;
    color: var(--brand-blue);
  }
</style>
</head>
<body>

  <section class="card card-back" aria-label="Card back">
    <p class="company-name-large">VUP</p>
  </section>

  <section class="card card-front" aria-label="Card front">
    <div class="rule"></div>

    <p class="company-name">VUP</p>

    <p class="person">Lena Baumgartner</p>

    <div class="icons">
      <svg viewBox="0 0 24 24" aria-label="Address">
        <circle cx="12" cy="12" r="11" fill="var(--brand-blue)"/>
        <path d="M12 5.5a4 4 0 0 0-4 4c0 3 4 8 4 8s4-5 4-8a4 4 0 0 0-4-4z" fill="none" stroke="#fff" stroke-width="1.5"/>
        <circle cx="12" cy="9.5" r="1.4" fill="#fff"/>
      </svg>
      <svg viewBox="0 0 24 24" aria-label="Phone">
        <circle cx="12" cy="12" r="11" fill="var(--brand-blue)"/>
        <path d="M8.5 6.5l2 2-1.2 1.5a7 7 0 0 0 4.7 4.7l1.5-1.2 2 2-1.5 1.5c-4.5 0-9-4.5-9-9z" fill="#fff"/>
      </svg>
      <svg viewBox="0 0 24 24" aria-label="Mobile">
        <circle cx="12" cy="12" r="11" fill="var(--brand-blue)"/>
        <rect x="8.5" y="5.5" width="7" height="13" rx="1.2" fill="none" stroke="#fff" stroke-width="1.5"/>
        <circle cx="12" cy="16" r=".8" fill="#fff"/>
      </svg>
      <svg viewBox="0 0 24 24" aria-label="Email">
        <circle cx="12" cy="12" r="11" fill="var(--brand-blue)"/>
        <rect x="6.5" y="8" width="11" height="8" rx="1" fill="none" stroke="#fff" stroke-width="1.4"/>
        <path d="M6.8 8.4L12 12.5l5.2-4.1" fill="none" stroke="#fff" stroke-width="1.4"/>
      </svg>
    </div>

    <div class="details">
      <p>VU Digital Pathways GmbH</p>
      <p>Lindenweg 12, CH-8400 Winterthur</p>
      <p>079 000 11 20<span class="sep">|</span>079 000 22 40<span class="sep">|</span>lena.baumgartner@vup.ch</p>
    </div>

    <p class="website">WWW.VUP.CH</p>
  </section>

</body>
</html>
```